Business Card Design for new logo

Business card Design for new logo. Follow colors from logo.
The company has offices in multiple comtries
Want to have some bulltes on the countries and also on the main services

Something like
USA*Dominican Republic*LATAM

Consulting*Healthcare IT*Tranformation

Industry/Entity Type

Information Technology

Contact Information for Business Card

Address, Phones, countries, name and position

Miron castell

Founder and CEO

947 Quarry Ln
Mill haven, PA 16835

Mcastell@novelquin.com

www.novelquin.com

717-352-6081

828-444-4444

```html
<!DOCTYPE html>
<html lang="en">
<head>
<meta charset="utf-8">
<title>Novelquin — Business Card</title>
<link rel="stylesheet" href="https://fonts.googleapis.com/css2?family=Montserrat:wght@400;500;600&family=Philosopher:wght@700&display=swap">
<style>
  :root {
    --backdrop: #151515;
    --card: #262626;
    --card-edge: #2e2e2e;
    --blue: #2a7fc4;
    --orange: #f08a4b;
    --ink: #f2f2f2;
    --muted: #c9c9c9;
    --silver: #8e8e8e;
  }
  * { margin: 0; padding: 0; box-sizing: border-box; }
  html, body { width: 1200px; height: 900px; overflow: hidden; }
  body {
    background: radial-gradient(ellipse at 55% 35%, #2a2a2a 0%, var(--backdrop) 70%);
    font-family: "Montserrat", sans-serif;
    color: var(--ink);
  }
  .stack {
    position: absolute;
    left: 250px; top: 40px;
    display: flex; flex-direction: column; gap: 30px;
  }
  .card {
    width: 700px; height: 400px;
    background: linear-gradient(135deg, var(--card-edge), var(--card) 60%, #202020);
    box-shadow: 0 14px 30px rgba(0,0,0,.55);
    position: relative;
  }
  .card-back {
    display: flex; align-items: center; justify-content: center;
  }
  .wordmark {
    display: flex; align-items: center; gap: 16px;
    font-family: "Philosopher", sans-serif; font-weight: 700;
  }
  .wordmark-dot { border-radius: 50%; }
  .card-back .wordmark { color: var(--silver); font-size: 54px; }
  .card-back .wordmark-dot { width: 40px; height: 40px; background: var(--silver); }
  .card-front { display: flex; align-items: center; }
  .brand-side {
    width: 360px;
    display: flex; flex-direction: column; align-items: center;
  }
  .card-front .wordmark { color: var(--blue); font-size: 48px; }
  .card-front .wordmark-dot { width: 34px; height: 34px; background: var(--blue); }
  .focus-lines {
    list-style: none;
    margin-top: 22px;
    text-align: center;
  }
  .focus-lines li {
    font-size: 12.5px; line-height: 1.9; letter-spacing: .4px;
    color: var(--muted);
    white-space: nowrap;
  }
  .sep { color: var(--orange); margin: 0 6px; }
  .divider {
    width: 2px; height: 240px; background: var(--orange);
  }
  .contact { padding-left: 34px; }
  .person-name {
    font-family: "Philosopher", sans-serif; font-weight: 700;
    color: var(--blue); font-size: 34px; line-height: 1;
  }
  .person-role { font-size: 17px; margin-top: 6px; letter-spacing: .5px; }
  .address { font-size: 17px; line-height: 1.4; margin-top: 16px; letter-spacing: .4px; }
  .lines { list-style: none; margin-top: 14px; }
  .lines li {
    display: flex; align-items: center; gap: 10px;
    font-size: 17px; line-height: 1.55; letter-spacing: .4px;
  }
  .lines svg { width: 15px; height: 15px; flex: none; stroke: var(--blue); fill: none; stroke-width: 1.8; }
  .web-name { color: var(--orange); }
</style>
</head>
<body>
<main class="stack">
  <section class="card card-back">
    <div class="wordmark"><span class="wordmark-dot"></span>Novelquin</div>
  </section>

  <section class="card card-front">
    <div class="brand-side">
      <div class="wordmark"><span class="wordmark-dot"></span>Novelquin</div>
      <ul class="focus-lines">
        <li>USA<span class="sep">•</span>Dominican Republic<span class="sep">•</span>LATAM</li>
        <li>Consulting<span class="sep">•</span>Healthcare IT<span class="sep">•</span>Transformation</li>
      </ul>
    </div>
    <div class="divider"></div>
    <div class="contact">
      <h1 class="person-name">Miron castell</h1>
      <p class="person-role">Founder and CEO</p>
      <p class="address">947 Quarry Ln<br>Mill haven, PA 16835</p>
      <ul class="lines">
        <li>
          <svg viewBox="0 0 16 16"><path d="M4 1.5l2.5 3-1.5 2c1 2 2.5 3.5 4.5 4.5l2-1.5 3 2.5-1.5 2.5C7 14 2 9 1.5 3z"/></svg>
          717-352-6081
        </li>
        <li>
          <svg viewBox="0 0 16 16"><rect x="4" y="1.5" width="8" height="13" rx="1.5"/><line x1="7" y1="12" x2="9" y2="12"/></svg>
          828-444-4444
        </li>
        <li>
          <svg viewBox="0 0 16 16"><rect x="1.5" y="3.5" width="13" height="9" rx="1"/><path d="M1.5 4l6.5 5 6.5-5"/></svg>
          Mcastell@novelquin.com
        </li>
        <li>
          <svg viewBox="0 0 16 16"><circle cx="8" cy="8" r="6.5"/><ellipse cx="8" cy="8" rx="3" ry="6.5"/><line x1="1.5" y1="8" x2="14.5" y2="8"/></svg>
          <span>www.<span class="web-name">novelquin</span>.com</span>
        </li>
      </ul>
    </div>
  </section>
</main>
</body>
</html>
```